RKT Capability Statement Brochure

We need a four or six-page flyer/brochure for our capability statement. This should include all the key written copy and photos/descriptions of the personnel, plus contact addresses in the current capability statement which is attached. We are looking for a modern, professional design that matches our professional approach to our business. Please incorporate our logo into the design.

Target Market(s)

Government departments, shipping companies, port operators, lawyers, export and import businesses, commodity companies.

Industry/Entity Type

Business Consultant

Contact Information for Business Card

Professional, simple to read, uncomplicated.

Font styles to use
Serif
Sans Serif

Colors

Designer to choose colors to be used in the design.

Requirements
Must have
• Company logo
• KEY MESSAGE: Providing independent, expert, confidential and professional services.
• Description of company
• Description and photos of personnel.
• Contact details.
Should not have
• No cliches

```html
<!DOCTYPE html>
<html lang="en">
<head>
<meta charset="utf-8">
<title>RKT Capability Statement 2017</title>
<link href="https://fonts.googleapis.com/css2?family=Open+Sans:wght@400;600;700&family=Oswald:wght@500;600&display=swap" rel="stylesheet">
<style>
  :root {
    --navy: #232c44;
    --navy-soft: #2f3a58;
    --accent: #3f6fa6;
    --panel: #e7e7e3;
    --text: #5b6270;
    --heading: #232c44;
    --page: #ffffff;
    --backdrop: #eef1f3;
  }
  * { box-sizing: border-box; margin: 0; padding: 0; }
  html, body { width: 1200px; height: 700px; overflow: hidden; }
  body {
    background: var(--backdrop);
    font-family: "Open Sans", Arial, sans-serif;
    color: var(--text);
    position: relative;
  }
  .spread {
    position: absolute;
    left: 40px; top: 140px;
    width: 1120px; height: 420px;
    display: flex;
  }
  .page { width: 560px; height: 420px; position: relative; overflow: hidden; }

  /* Back cover */
  .back-cover { background: var(--navy); }
  .contact-panel {
    position: absolute;
    left: 14px; top: 100px;
    width: 440px; height: 222px;
    background: var(--panel);
  }
  .intro {
    position: absolute;
    left: 14px; top: 10px; width: 412px;
    font-size: 7.5px; line-height: 1.4;
  }
  .contacts-banner {
    position: absolute;
    left: 0; top: 44px;
    width: 150px; height: 20px;
    background: var(--navy);
    color: #fff;
    font-family: "Oswald", Arial, sans-serif;
    font-weight: 600; font-size: 13px; letter-spacing: .5px;
    line-height: 20px; padding-left: 24px;
  }
  .brand {
    position: absolute; left: 168px; top: 38px;
    display: flex; align-items: center; gap: 6px;
    color: var(--navy);
  }
  .brand-mark { width: 14px; height: 14px; border-radius: 50%; background: var(--navy); }
  .brand-name { font-weight: 700; font-size: 22px; line-height: 1; }
  .brand-tag { font-weight: 700; font-size: 6px; letter-spacing: .8px; color: var(--navy); position: absolute; left: 188px; top: 62px; }
  .contact-cols {
    position: absolute; left: 0; top: 76px; width: 440px;
    display: flex;
  }
  .contact-col { width: 146px; padding: 0 10px 0 22px; font-size: 7px; line-height: 1.35; }
  .contact-col + .contact-col { border-left: 1px solid #b8b9b8; padding-left: 12px; }
  .region { font-weight: 700; color: var(--heading); font-size: 7.5px; margin-top: 8px; }
  .region:first-child { margin-top: 0; }
  .person { font-weight: 700; color: var(--heading); }
  .entity { font-weight: 700; color: var(--heading); margin-top: 12px; }
  .address { margin-top: 14px; }

  /* Front cover */
  .front-cover { background: var(--page); }
  .cover-photo { position: absolute; left: 0; top: 0; width: 560px; height: 300px; }
  .cover-brand {
    position: absolute; right: 20px; top: 18px;
    display: flex; align-items: center; gap: 5px; color: var(--navy);
  }
  .cover-brand .brand-mark { width: 10px; height: 10px; }
  .cover-brand .brand-name { font-size: 17px; }
  .key-message {
    position: absolute; left: 0; top: 282px;
    width: 330px; height: 44px;
    background: var(--navy);
    color: #fff;
    font-family: "Oswald", Arial, sans-serif;
    font-weight: 500; font-size: 13px; line-height: 17px; letter-spacing: .3px;
    padding: 5px 0 0 16px;
    border-left: 26px solid var(--accent);
  }
  .website { position: absolute; left: 42px; top: 340px; font-size: 6.5px; color: var(--text); }
  .cover-title {
    position: absolute; right: 20px; top: 312px;
    font-family: "Oswald", Arial, sans-serif;
    font-weight: 600; font-size: 17px; color: var(--navy); letter-spacing: .4px;
  }
</style>
</head>
<body>
<main class="spread">
  <section class="page back-cover">
    <div class="contact-panel">
      <p class="intro">RKT has acted as broker for significant multimillion-dollar ship acquisitions for the nation and provided advice and analysis on projects ranging from market research through to sale of surplus Defence Department marine assets.</p>
      <div class="contacts-banner">CONTACTS US</div>
      <div class="brand"><span class="brand-mark"></span><span class="brand-name">RKT</span></div>
      <div class="brand-tag">ROCKETT KEEL TRADING</div>
      <div class="contact-cols">
        <div class="contact-col">
          <p class="region">VICTORIA</p>
          <p class="person">Daniel Reyes</p>
          <p>Tel: +61 400 100 201</p>
          <p>e: daniel@rktadvisory.com</p>
          <p class="region">VICTORIA</p>
          <p class="person">Megan Holt</p>
          <p>Tel: +61 400 100 202</p>
          <p>e: megan@rktadvisory.com</p>
          <p class="entity">Rockett Keel Trading Pty Ltd.<br>Atf RKT Group Unit Trust<br>ABN: 00 000 000 000</p>
        </div>
        <div class="contact-col">
          <p class="region">NEW SOUTH WALES</p>
          <p class="person">Owen Prescott</p>
          <p>Tel: +61 400 100 203</p>
          <p>e: owen@rktadvisory.com</p>
          <p class="region">TASMANIA</p>
          <p class="person">Liam Kerr</p>
          <p>Tel: +61 400 100 204</p>
          <p>e: liam@rktadvisory.com</p>
          <p class="address">Registered Address:<br>Rockett Keel Trading Pty Ltd.,<br>42 Harbour Lane, Seaford,<br>Victoria 3198.</p>
        </div>
        <div class="contact-col">
          <p class="region">QUEENSLAND</p>
          <p class="person">Grant Fowler</p>
          <p>Tel: +61 400 100 205</p>
          <p>e: grant@rktadvisory.com</p>
          <p class="address" style="margin-top:46px">Telephone: +61 3 9000 0101<br>Fax: +61 3 9000 0102<br>info@rktadvisory.com</p>
        </div>
      </div>
    </div>
  </section>

  <section class="page front-cover">
    <svg class="cover-photo" role="img" aria-label="Photo of a red offshore support vessel moored in a city harbour" viewBox="0 0 560 300" preserveAspectRatio="none">
      <defs>
        <linearGradient id="harbour" x1="0" y1="0" x2="0" y2="1">
          <stop offset="0" stop-color="#c9d3df"/>
          <stop offset="0.5" stop-color="#8c9aab"/>
          <stop offset="0.7" stop-color="#4a4f5a"/>
          <stop offset="1" stop-color="#2e3f55"/>
        </linearGradient>
      </defs>
      <rect width="560" height="300" fill="url(#harbour)"/>
    </svg>
    <div class="cover-brand"><span class="brand-mark"></span><span class="brand-name">RKT</span></div>
    <div class="key-message">PROVIDING INDEPENDENT, EXPERT,<br>CONFIDENTIAL AND PROFESSIONAL SERVICES</div>
    <p class="website">www.rktadvisory.com</p>
    <p class="cover-title">CAPABILITY STATEMENT 2017</p>
  </section>
</main>
</body>
</html>
```